I'm a magician . hypnotist also a good barber. I need this all to be shown in good detail on the cards.

Magician

Magician/ hypnotist/barber Morris quill. One of the best. Tel 07412 638204
Email.Velvetowl27@postmail-example.net
Title of card velvet owl.

```html
<!DOCTYPE html>
<html lang="en">
<head>
<meta charset="utf-8">
<title>VelvetOwl – Magician, Hypnotist &amp; Barber</title>
<link rel="stylesheet" href="https://fonts.googleapis.com/css2?family=Jost:wght@400&family=Open+Sans:wght@400&display=swap">
<style>
  :root {
    --wall-light: #ebebe9;
    --wall-mid: #cfd0ce;
    --wall-dark: #a3a5a4;
    --suit: #1d1e22;
    --tone-violet: #7d3ad0;
    --tone-blue: #2f4fd6;
    --tone-red: #de3a1e;
    --tone-orange: #f0a020;
    --ink: #111111;
  }
  * { margin: 0; padding: 0; box-sizing: border-box; }
  html, body {
    width: 1200px;
    height: 791px;
    overflow: hidden;
    background: #ffffff;
  }
  .card {
    position: relative;
    width: 1200px;
    height: 791px;
    overflow: hidden;
    background: radial-gradient(ellipse 760px 560px at 340px 320px, var(--wall-light) 0%, var(--wall-mid) 60%, var(--wall-dark) 100%);
  }
  .hero-photo {
    position: absolute;
    top: 0;
    right: 0;
    width: 620px;
    height: 791px;
    background: linear-gradient(160deg, var(--tone-blue) 0%, var(--tone-violet) 22%, var(--tone-red) 48%, var(--tone-orange) 66%, var(--suit) 100%);
    -webkit-mask-image: linear-gradient(90deg, transparent 0%, #000 30%);
    mask-image: linear-gradient(90deg, transparent 0%, #000 30%);
  }
  .text {
    position: absolute;
    left: 46px;
    font-family: "Open Sans", sans-serif;
    font-weight: 400;
    line-height: 1;
    color: var(--ink);
  }
  .title-role { top: 40px; left: 44px; font-size: 55px; }
  .phone { top: 118px; left: 48px; font-size: 29px; }
  .brand-name {
    top: 405px;
    left: 40px;
    font-family: "Jost", sans-serif;
    font-size: 124px;
    letter-spacing: -1px;
  }
  .email { top: 566px; font-size: 25px; }
  .services { top: 612px; font-size: 25px; }
</style>
</head>
<body>
  <main class="card">
    <div class="hero-photo" role="img" aria-label="Photograph of a magician in a dark suit pulling a burst of rainbow paint out of a blue top hat"></div>
    <p class="text title-role">Magician</p>
    <p class="text phone">Tel 07412 638204</p>
    <h1 class="text brand-name">VelvetOwl</h1>
    <p class="text email">Email: Velvetowl27@postmail-example.net</p>
    <p class="text services">Morris Quill · Hypnotist &amp; Barber</p>
  </main>
</body>
</html>
```